6 - 8 'Holistic' Instagram Graphics

Hi there!
We are looking to build up a library of Graphic Templates to use as Instagram & Facebook posts for our Holistic Medi Spa (& 3 other companies eventually)
This competition is for a sample of 6 - 8 designs. For the winner(s), we will make an agreement for a batch order (Looking for 200+ designs in total), and will be looking to make a long term arrangement.
Please find a full job description in the attached Word Document.
Any questions, don't hesitate to ask.
Thanks!
Medical Spa

```html
<!DOCTYPE html>
<html lang="en">
<head>
<meta charset="utf-8">
<title>Customer Testimonial – Willow Loft</title>
<link rel="stylesheet" href="https://fonts.googleapis.com/css2?family=Josefin+Sans:wght@300;400&family=Libre+Baskerville:wght@700&display=swap">
<style>
  :root {
    --mint-light: #eef9f6;
    --mint: #d9f1ea;
    --mint-deep: #bfe3d6;
    --foliage: rgba(86, 150, 118, 0.55);
    --foliage-soft: rgba(150, 200, 175, 0.25);
    --gold: #d8bf9f;
    --card: rgba(250, 252, 251, 0.9);
    --name: #77746c;
    --body: #8b8881;
    --ring: #878679;
    --photo: #d9b8aa;
    --email: #8e9893;
  }
  * { margin: 0; padding: 0; box-sizing: border-box; }
  html, body { width: 1200px; height: 1200px; overflow: hidden; }
  body {
    position: relative;
    background:
      radial-gradient(ellipse 420px 300px at 150px 780px, rgba(191, 227, 214, 0.55), transparent 70%),
      radial-gradient(ellipse 460px 360px at 1000px 430px, rgba(191, 227, 214, 0.45), transparent 70%),
      radial-gradient(ellipse 380px 260px at 560px 140px, rgba(255, 255, 255, 0.6), transparent 70%),
      linear-gradient(160deg, var(--mint-light), var(--mint) 55%, var(--mint-light));
    font-family: "Josefin Sans", sans-serif;
  }

  .foliage-wash {
    position: absolute;
    width: 340px;
    height: 340px;
    border-radius: 50%;
    background: radial-gradient(circle, var(--foliage) 0%, var(--foliage-soft) 45%, transparent 70%);
  }
  .foliage-wash--top-left { left: -110px; top: -110px; }
  .foliage-wash--top-right { right: -110px; top: -110px; }
  .foliage-wash--bottom-left { left: -110px; bottom: -110px; }
  .foliage-wash--bottom-right { right: -110px; bottom: -110px; }

  .headline {
    position: absolute;
    left: 264px;
    top: 100px;
    color: var(--gold);
    font-weight: 400;
    font-size: 106px;
    line-height: 96px;
    letter-spacing: 1px;
  }

  .testimonial-card {
    position: absolute;
    left: 267px;
    top: 346px;
    width: 783px;
    height: 587px;
    background: var(--card);
    border-radius: 14px;
    box-shadow: 0 18px 30px rgba(90, 130, 115, 0.12);
  }
  .testimonial-card__name {
    position: absolute;
    left: 177px;
    top: 48px;
    font-family: "Libre Baskerville", serif;
    font-weight: 700;
    font-size: 27px;
    color: var(--name);
  }
  .testimonial-card__quote {
    position: absolute;
    left: 177px;
    top: 100px;
    font-weight: 300;
    font-size: 32px;
    line-height: 40px;
    color: var(--body);
  }
  .rating {
    position: absolute;
    left: 414px;
    top: 508px;
    display: flex;
    align-items: center;
    gap: 10px;
  }
  .rating__score {
    font-family: "Libre Baskerville", serif;
    font-weight: 700;
    font-size: 26px;
    color: var(--name);
    margin-right: 26px;
  }

  .client-photo {
    position: absolute;
    left: 150px;
    top: 611px;
    width: 234px;
    height: 234px;
    border-radius: 50%;
    border: 20px solid var(--ring);
    background: radial-gradient(circle at 55% 45%, #f1dcd2, var(--photo) 70%, #b98f80);
  }

  .contact-email {
    position: absolute;
    left: 0;
    width: 1200px;
    top: 1106px;
    text-align: center;
    font-weight: 300;
    font-size: 52px;
    line-height: 60px;
    letter-spacing: 3px;
    color: var(--email);
  }
</style>
</head>
<body>
  <div class="foliage-wash foliage-wash--top-left" role="img" aria-label="Green watercolour foliage accent"></div>
  <div class="foliage-wash foliage-wash--top-right" role="img" aria-label="Green watercolour foliage accent"></div>
  <div class="foliage-wash foliage-wash--bottom-left" role="img" aria-label="Green watercolour foliage accent"></div>
  <div class="foliage-wash foliage-wash--bottom-right" role="img" aria-label="Green watercolour foliage accent"></div>

  <h1 class="headline">Customer<br>Testimonial</h1>

  <section class="testimonial-card">
    <h2 class="testimonial-card__name">Marian Holt</h2>
    <p class="testimonial-card__quote">
      I received a very professional<br>
      analysis of my facial skin care<br>
      needs. The facial was noticed<br>
      immediately by my husband. He said<br>
      I was glowing!! The products I<br>
      purchased make my home daily<br>
      care simple; just what I needed for<br>
      my busy lifestyle. Thank you Willow<br>
      Loft!!!!
    </p>
    <div class="rating">
      <span class="rating__score">5</span>
      <svg class="rating__stars" width="260" height="44" viewBox="0 0 260 44" aria-label="Five stars">
        <defs>
          <path id="star" d="M22 2 L27.6 15.8 L42.5 16.8 L31 26.3 L34.7 40.8 L22 32.8 L9.3 40.8 L13 26.3 L1.5 16.8 L16.4 15.8 Z"/>
        </defs>
        <use href="#star" x="0" fill="#d8bf9f"/>
        <use href="#star" x="52" fill="#d8bf9f"/>
        <use href="#star" x="104" fill="#d8bf9f"/>
        <use href="#star" x="156" fill="#d8bf9f"/>
        <use href="#star" x="208" fill="#d8bf9f"/>
      </svg>
    </div>
  </section>

  <div class="client-photo" role="img" aria-label="Portrait of the client, hands touching her hair"></div>

  <p class="contact-email">care@willowloft.com</p>
</body>
</html>
```